Stationery Design Project

Need stationery designed for our chicken farming business. We grow chickens in barns for meat production. Looking for all stationery items (business cards, letterhead, envelopes, with compliments etc).
Updates

Reason: I am going away for 5 days from Friday 30/3/2012. Won't be able to check designs.

Target Market(s)

The stationery will only be used for correspondence with key stakeholders / suppliers. It is not to be used for marketing etc.

Industry/Entity Type

Business

Requirements
Must have
• I have included all the contact details required for each type of stationery.
Nice to have
• Colours to be used white, green, red, yellow and black (see design).
Should not have
• Rounded Corners.
Centralised information (in centre of business cards / letterhead etc).

```html
<!DOCTYPE html>
<html lang="en">
<head>
<meta charset="utf-8">
<title>Brookvale Poultry – With Compliments Slip</title>
<link rel="stylesheet" href="https://fonts.googleapis.com/css2?family=Open+Sans:wght@400;600&family=Tinos:ital,wght@1,700&display=swap">
<style>
  :root {
    --farm-green: #1d6b45;
    --farm-green-soft: #3f8a62;
    --barn-red: #9b1b24;
    --sun-yellow: #f2a516;
    --ink-grey: #555555;
    --paper: #ffffff;
  }
  * { margin: 0; padding: 0; box-sizing: border-box; }
  html, body {
    width: 1200px;
    height: 641px;
    overflow: hidden;
    background: var(--paper);
  }
  .slip {
    position: relative;
    width: 1200px;
    height: 641px;
    background: var(--paper);
    font-family: "Open Sans", Arial, sans-serif;
  }
  .brand {
    position: absolute;
    left: 96px;
    top: 94px;
    display: flex;
    align-items: center;
    gap: 16px;
  }
  .brand-dot {
    width: 44px;
    height: 44px;
    border-radius: 50%;
    background: var(--barn-red);
  }
  .brand-name {
    font-weight: 600;
    font-size: 34px;
    line-height: 1;
    color: var(--farm-green);
  }
  .greeting {
    position: absolute;
    left: 98px;
    top: 346px;
    font-family: "Tinos", "Times New Roman", serif;
    font-style: italic;
    font-weight: 700;
    font-size: 45px;
    line-height: 1;
    color: var(--farm-green);
  }
  .footer-band {
    position: absolute;
    left: 0;
    top: 0;
    width: 1200px;
    height: 641px;
  }
  .postal {
    position: absolute;
    left: 123px;
    top: 470px;
    width: 360px;
    text-align: center;
    font-style: normal;
    font-size: 18px;
    line-height: 37px;
    color: var(--ink-grey);
  }
  .contact {
    position: absolute;
    right: 52px;
    top: 470px;
    list-style: none;
    font-size: 18px;
    line-height: 31px;
    color: var(--sun-yellow);
  }
  .contact li {
    display: flex;
    justify-content: flex-end;
    align-items: center;
    gap: 14px;
  }
  .contact-icon {
    width: 20px;
    height: 20px;
    fill: none;
    stroke: var(--paper);
    stroke-width: 2;
  }
  .contact-icon text {
    fill: var(--paper);
    stroke: none;
  }
</style>
</head>
<body>
<main class="slip">
  <svg class="footer-band" viewBox="0 0 1200 641" role="img" aria-label="Decorative footer wave in farm green, red and yellow tones">
    <defs>
      <linearGradient id="footer-fill" x1="0" y1="0" x2="1" y2="0">
        <stop offset="0" stop-color="var(--farm-green-soft)"/>
        <stop offset="1" stop-color="var(--farm-green)"/>
      </linearGradient>
    </defs>
    <path fill="url(#footer-fill)"
          d="M0,596 C400,606 800,505 1200,420 L1200,641 L0,641 Z"/>
  </svg>

  <div class="brand">
    <span class="brand-dot"></span>
    <span class="brand-name">Brookvale Poultry Pty Ltd</span>
  </div>

  <h1 class="greeting">With Compliments</h1>

  <address class="postal">
    PO Box 472, RIVERTON SA 5412<br>
    Millers Flat Road HOLLOWAY SA 5264
  </address>

  <ul class="contact">
    <li>0400 123 456
      <svg class="contact-icon" viewBox="0 0 20 20" aria-hidden="true">
        <circle cx="10" cy="10" r="8"/>
        <path d="M7,6 C6,9 8,13 12,14 L13,12.5 L11.5,11.5 L10.5,12 C9,11 8.5,10 8.2,8.8 L9,8 L8,6 Z" stroke-width="1.2"/>
      </svg>
    </li>
    <li>08 8500 0142
      <svg class="contact-icon" viewBox="0 0 20 20" aria-hidden="true">
        <path d="M3,8 C3,5 17,5 17,8 L14,9 L13,7.5 L7,7.5 L6,9 Z"/>
        <rect x="5" y="10" width="10" height="6" rx="1"/>
      </svg>
    </li>
    <li>office@brookvalepoultry.com
      <svg class="contact-icon" viewBox="0 0 20 20" aria-hidden="true">
        <text x="10" y="15.5" text-anchor="middle" font-size="17" font-family="Open Sans, Arial, sans-serif">@</text>
      </svg>
    </li>
  </ul>
</main>
</body>
</html>
```